Upscale business cards needed for Board of Directors

We need professional business cards created for members of our family business Board of Directors. We would like these relatively simple and straightforward, but also with a unique element to set them apart. Probably stick with neutral and simple colors - white, grey etc. We need space for the traditional elements, including name, title, address, email/phone number. And we will be creating several from this template so it needs to be template that is easy to switch information in and out of.
Business
See description

```html
<!DOCTYPE html>
<html lang="en">
<head>
<meta charset="utf-8">
<title>Harborline Holdings — Business Cards</title>
<link href="https://fonts.googleapis.com/css2?family=Lato:wght@400;700;900&display=swap" rel="stylesheet">
<style>
  :root {
    --backdrop: #3b3b3c;
    --card-dark: #1f1e1e;
    --card-light: #ffffff;
    --ink: #1d1d1d;
    --ink-soft: #3a3a3a;
    --gold: #b09a6e;
    --white: #ffffff;
  }
  * { margin: 0; padding: 0; box-sizing: border-box; }
  html, body {
    width: 1200px; height: 810px; overflow: hidden;
    background: var(--backdrop);
    font-family: "Lato", Arial, sans-serif;
  }
  .stage {
    width: 1200px; height: 810px;
    display: flex; flex-direction: column;
    align-items: center; justify-content: center; gap: 34px;
  }
  .card {
    position: relative;
    width: 630px; height: 360px;
    box-shadow: 0 10px 24px rgba(0,0,0,.35);
  }
  /* Back side */
  .card--back { background: var(--card-dark); color: var(--white); }
  .card--back .wordmark {
    position: absolute; left: 0; right: 0; top: 128px;
    text-align: center;
    font-weight: 900; font-size: 40px; letter-spacing: 1px; line-height: 1.1;
    color: var(--white);
  }
  .card--back .wordmark small {
    display: block; font-size: 22px; letter-spacing: 10px; margin-top: 6px; font-weight: 900;
  }
  .card--back .web {
    position: absolute; left: 0; right: 0; bottom: 64px;
    text-align: center; font-size: 14px; letter-spacing: .3px;
  }
  /* Front side */
  .card--front { background: var(--card-light); color: var(--ink); }
  .card--front .wordmark {
    position: absolute; right: 36px; top: 40px;
    text-align: right;
    font-weight: 900; font-size: 34px; letter-spacing: 1px; line-height: 1.1;
    color: var(--ink);
  }
  .card--front .wordmark small {
    display: block; font-size: 18px; letter-spacing: 9px; margin-top: 4px; font-weight: 900;
  }
  .person { position: absolute; left: 40px; top: 190px; }
  .person__name {
    font-size: 20px; font-weight: 400; letter-spacing: .6px;
    color: var(--gold); text-transform: uppercase;
  }
  .person__title { font-size: 15px; color: var(--ink-soft); margin-top: 2px; }
  .contacts { list-style: none; margin-top: 18px; }
  .contacts li {
    display: flex; align-items: center; gap: 10px;
    font-size: 15px; color: var(--ink); line-height: 1.55;
  }
  .contacts svg { width: 14px; height: 14px; fill: var(--gold); flex: none; }
  .address {
    position: absolute; right: 36px; top: 196px;
    text-align: right; font-size: 14px; line-height: 1.45; color: var(--ink-soft);
  }
  .band {
    position: absolute; left: 0; right: 0; bottom: 0; height: 16px;
    background: var(--gold);
  }
</style>
</head>
<body>
<main class="stage">
  <section class="card card--back" aria-label="Card back">
    <div class="wordmark">HARBORLINE<small>HOLDINGS</small></div>
    <p class="web">www.harborlineholdings.com</p>
  </section>

  <section class="card card--front" aria-label="Card front">
    <div class="wordmark">HARBORLINE<small>HOLDINGS</small></div>

    <div class="person">
      <h1 class="person__name">Julien Marlowe</h1>
      <p class="person__title">CEO &amp; President</p>
      <ul class="contacts">
        <li>
          <svg viewBox="0 0 16 16" aria-hidden="true"><path d="M3.2 1.5l2.4-.4 1.3 3.3-1.6 1.2a8 8 0 0 0 4.9 4.9l1.2-1.6 3.3 1.3-.4 2.4c-.2.8-1 1.3-1.8 1.2C6.9 13.3 2.7 9.1 2 3.3c-.1-.8.4-1.6 1.2-1.8z"/></svg>
          +212 522 40 17 63
        </li>
        <li>
          <svg viewBox="0 0 16 16" aria-hidden="true"><path d="M5 1h6a1.5 1.5 0 0 1 1.5 1.5v11A1.5 1.5 0 0 1 11 15H5a1.5 1.5 0 0 1-1.5-1.5v-11A1.5 1.5 0 0 1 5 1zm0 2v9h6V3H5zm3 10a.8.8 0 1 0 0 1.6A.8.8 0 0 0 8 13z"/></svg>
          +212 522 40 18 25
        </li>
        <li>
          <svg viewBox="0 0 16 16" aria-hidden="true"><path d="M1 3.5h14v9H1zm1.6 1.2L8 8.6l5.4-3.9H2.6zm-.3 1.5v5h11.4v-5L8 10.2z"/></svg>
          contact@harborlineholdings.com
        </li>
        <li>
          <svg viewBox="0 0 16 16" aria-hidden="true"><path d="M8 1a7 7 0 1 0 0 14A7 7 0 0 0 8 1zm5.4 6.3h-2.5a11 11 0 0 0-1.2-4.6 5.6 5.6 0 0 1 3.7 4.6zM8 2.5c.8 1 1.4 2.7 1.5 4.8h-3C6.6 5.2 7.2 3.5 8 2.5zM6.3 2.7a11 11 0 0 0-1.2 4.6H2.6a5.6 5.6 0 0 1 3.7-4.6zM2.6 8.7h2.5a11 11 0 0 0 1.2 4.6 5.6 5.6 0 0 1-3.7-4.6zM8 13.5c-.8-1-1.4-2.7-1.5-4.8h3c-.1 2.1-.7 3.8-1.5 4.8zm1.7-.2a11 11 0 0 0 1.2-4.6h2.5a5.6 5.6 0 0 1-3.7 4.6z"/></svg>
          www.harborlineholdings.com
        </li>
      </ul>
    </div>

    <address class="address" style="font-style:normal">
      58 rue 12 Quartier<br>
      Les Jardins, Rabat
    </address>

    <div class="band"></div>
  </section>
</main>
</body>
</html>
```